www.HarborviewSmileGlow.com needs to be re-designed

Current website to be redesigned www.HarborviewSmileGlow.com

*Need a custom-made new theme

I need all 10 pages redesigned using existing content.
I need the website to be revamped to a more modern look.

Please start with Homepage first then after homepage mock up is approved we can move forward with rest of pages.

Please use existing images from my Facebook or Instagram page of our real customers for banner image...

(Where to find my FB and IG pages...
You can access these pages from the website header and "contact us" page for address.)

I would like to have a button that says "Book Appointment Online" and get rid of the actual form that is on current website.

But other than that please include all other content, features, etc in mock ups so I can make a decision on the website.

I prefer custom design and must be WP installable responsive theme.

This is design-only. I am open to any concepts you can submit.

Target Market(s)

people that care about thier looks

Industry/Entity Type

Dental Clinic

Colors

Designer to choose colors to be used in the design.

Requirements
Must have
• All current content/text that is currently on website. Just formatted so it doesnt look so busy. I want to make emphasis on BOOK APPOINTMENT button and $99 SPECIAL BUTTON
Nice to have
• White background so everything pops
Should not have
• I do not like stock photo images, please use images from my facebook and IG page of real customers or even a snap shot of our office building. You can access these pages from the website header and contact us page for address, maybe yu can use snapshot somewhere of building of our address on homepage possibly in banner image.

```html
<!DOCTYPE html>
<html lang="en">
<head>
<meta charset="utf-8">
<title>Harborview Smile Glow – Home</title>
<link href="https://fonts.googleapis.com/css2?family=Roboto:wght@300;400;500;700;900&family=Open+Sans:wght@400;600&display=swap" rel="stylesheet">
<style>
:root{
  --blue:#29a9e6;
  --blue-dark:#1c8fcc;
  --ink:#222;
  --text:#555;
  --grey-dark:#4d4d4d;
  --black:#0d0d0d;
  --white:#fff;
  --accent:#ffd24a;
}
*{margin:0;padding:0;box-sizing:border-box}
html,body{width:1200px;height:2980px;overflow:hidden;background:var(--white)}
body{font-family:"Roboto",Arial,sans-serif;color:var(--ink);position:relative}
.page{position:relative;width:1200px;height:2980px;overflow:hidden}
.abs{position:absolute}
h1,h2,h3{font-weight:400}

/* header */
.brand{left:78px;top:24px;display:flex;align-items:center;gap:14px}
.brand-dot{width:70px;height:70px;border-radius:50%;background:#d9dde2}
.brand-name{font-size:34px;font-weight:500;color:var(--blue-dark);line-height:1}
.phone{left:696px;top:20px;font-size:17px;color:var(--ink);display:flex;align-items:center;gap:10px}
.btn-book-top{left:872px;top:0;width:254px;height:52px;background:var(--blue);color:var(--white);border-radius:0 0 10px 10px;font-size:16px;font-weight:700;letter-spacing:.3px;display:flex;align-items:center;justify-content:center;box-shadow:0 6px 12px rgba(41,169,230,.35)}
.special{left:676px;top:66px;display:flex;align-items:center;gap:10px;font-size:17px;font-weight:700;font-style:italic}
.btn-special{font-style:normal;font-size:14px;font-weight:700;color:var(--ink);background:var(--accent);border-radius:16px;padding:6px 14px;box-shadow:0 3px 6px rgba(0,0,0,.15)}
.btn-special span{font-weight:400;color:#555}

.nav{left:0;top:114px;width:1200px;height:54px;background:var(--blue);display:flex;align-items:center;padding-left:78px}
.nav a{color:var(--white);text-decoration:none;font-size:14px;padding:0 22px;height:54px;line-height:54px}
.nav a.active{background:var(--grey-dark)}

/* hero */
.hero{left:0;top:168px;width:1200px;height:547px;background:linear-gradient(90deg,#cfc9c2 0%,#efece8 40%,#f3efea 70%,#d8cfc6 100%)}
.hero-title{left:550px;top:268px;font-size:36px;font-weight:900;line-height:1.18;color:#111}
.hero-list{left:552px;top:364px;list-style:none}
.hero-list li{font-size:24px;font-weight:300;color:#333;margin-bottom:8px;display:flex;align-items:center;gap:12px}

/* booking card */
.appt-head{left:790px;top:574px;width:336px;height:140px;background:linear-gradient(#666,#3f3f3f);border-radius:14px 14px 0 0;text-align:center;color:var(--white);padding-top:18px}
.appt-head h3{font-size:26px;font-weight:700;line-height:1.2}
.appt-head p{font-size:18px;margin-top:8px}
.appt-body{left:790px;top:714px;width:336px;height:190px;background:var(--blue);border-radius:0 0 14px 14px;padding:32px 26px 0;box-shadow:0 10px 18px rgba(0,0,0,.22);display:flex;flex-direction:column;gap:16px}
.btn-online{height:56px;border-radius:28px;background:var(--white);color:var(--blue-dark);font-size:17px;font-weight:700;display:flex;align-items:center;justify-content:center;gap:10px;box-shadow:0 4px 8px rgba(0,0,0,.18)}
.btn-deal{height:56px;border-radius:28px;background:var(--accent);color:var(--ink);font-size:17px;font-weight:700;display:flex;align-items:center;justify-content:center;gap:8px;box-shadow:0 4px 8px rgba(0,0,0,.18)}
.btn-deal span{font-weight:400;font-size:14px;color:#555}

/* intro */
.intro{left:80px;top:764px;width:690px}
.intro h1{font-size:31px;font-weight:400;color:var(--blue)}
.intro h2{font-size:23px;font-weight:400;color:#333;margin:18px 0 10px}
.intro p{font-family:"Open Sans",sans-serif;font-size:12.5px;line-height:1.6;color:var(--text);margin-bottom:16px}

/* how it works */
.how{left:0;top:1090px;width:1200px;height:390px;background:radial-gradient(circle at 30% 40%,#f5f9fe 0,#dfeaf8 60%,#cfe1f4 100%)}
.how-band{left:0;top:1410px;width:1200px;height:70px;background:var(--blue)}
.how-band span{position:absolute;left:550px;top:15px;font-size:32px;font-weight:400;color:#111}
.video{left:78px;top:1196px;width:442px;height:296px;background:var(--white);box-shadow:0 8px 14px rgba(0,0,0,.3);padding:22px}
.video-img{width:398px;height:214px;background:linear-gradient(90deg,#d6cbbf,#eee4da 55%,#f6f4f2)}
.video-bar{width:398px;height:42px;background:var(--blue)}
.how-title{left:550px;top:1146px;font-size:30px;font-weight:400;color:#111}
.how-text{left:550px;top:1198px;width:580px;font-family:"Open Sans",sans-serif;font-size:13px;line-height:1.65;color:var(--text)}
.btn-more{left:548px;top:1318px;width:156px;height:52px;border:2px solid #333;border-radius:26px;background:var(--white);font-size:17px;display:flex;align-items:center;justify-content:center}

/* compare */
.compare-title{left:0;top:1544px;width:1200px;text-align:center;font-size:31px;font-weight:300;color:var(--blue)}
.cmp{left:78px;top:1606px;width:1046px;display:grid;grid-template-columns:repeat(5,1fr)}
.cmp .col{display:flex;flex-direction:column}
.cmp .head{height:110px;margin-top:8px;background:linear-gradient(#f6f6f6,#e2e2e2);display:flex;align-items:center;justify-content:center;font-size:32px;font-weight:300;border-right:1px solid #ccc}
.cmp .speed{height:60px;background:linear-gradient(#8a8a8a,#444);color:var(--white);font-size:18px;display:flex;align-items:center;justify-content:center;border-right:1px solid #999}
.cmp .cell{height:63px;background:linear-gradient(#f5f5f5,#e0e0e0);color:var(--blue);font-size:18px;display:flex;align-items:center;justify-content:center;border-right:1px solid #ccc;border-top:1px solid #fff}
.cmp .feat .head{margin-top:0;height:118px;background:var(--blue);color:var(--white);font-size:38px;font-weight:400}
.cmp .feat .cell{font-size:23px;background:linear-gradient(#fff,#e6e6e6);box-shadow:0 4px 6px rgba(0,0,0,.2)}
.cmp .feat .speed{font-size:23px;background:linear-gradient(#9a9a9a,#555)}
.cmp .brand-cell{font-size:22px;font-weight:500;color:#111;text-align:center;line-height:1.05}

/* testimonial */
.quote{left:214px;top:2086px;width:772px;height:150px;background:var(--blue);border-radius:10px;color:var(--white);text-align:center;font-size:16px;line-height:1.6;padding:30px 50px}
.quote-tail{left:588px;top:2234px}
.people{left:368px;top:2282px;width:464px;height:90px}
.av{position:absolute;border-radius:50%;border:3px solid #ddd}
.arrow-btn{position:absolute;top:24px;width:32px;height:32px;border-radius:50%;border:1px solid #bbb;color:#888;font-size:14px;display:flex;align-items:center;justify-content:center;background:#f4f4f4}

/* why */
.why{left:0;top:2424px;width:1200px;height:316px;background:linear-gradient(#f4f4f4,#e8eaec)}
.why-title{left:0;top:2470px;width:1200px;text-align:center;font-size:32px;font-weight:400;color:#111}
.why-row{left:76px;top:2534px;display:flex;gap:6px}
.why-card{width:204px;height:150px;background:var(--blue);border-radius:0 0 10px 10px;border-top:5px solid #333;display:flex;flex-direction:column;align-items:center;justify-content:flex-end;padding-bottom:14px;color:var(--white);font-size:18px;gap:12px}
.why-card.on{background:var(--white);color:var(--blue);box-shadow:0 6px 12px rgba(0,0,0,.18);border-top-color:var(--blue)}
.icon-ring{width:70px;height:70px;border-radius:50%;background:rgba(255,255,255,.25);display:flex;align-items:center;justify-content:center}
.why-card.on .icon-ring{background:#eee}

/* footer */
.footer{left:0;top:2740px;width:1200px;height:240px;background:var(--black);color:var(--white)}
.f-item{position:absolute;top:46px;display:flex;align-items:center;gap:16px;font-size:13.5px;line-height:1.7}
.f-icon{width:52px;height:52px;border-radius:50%;background:var(--white);display:flex;align-items:center;justify-content:center}
.f-rule{left:78px;top:144px;width:1046px;border-top:1px solid #666}
.f-links{left:78px;top:154px;font-size:11.5px;display:flex;gap:10px}
.f-links span{color:#999}
.social{left:78px;top:194px;display:flex}
.social div{width:50px;height:46px;background:#3a3a3a;border-right:1px solid #222;display:flex;align-items:center;justify-content:center}
.social div:first-child{background:var(--blue)}
.social i{display:block;width:14px;height:14px;border-radius:3px;background:#ccc}
.copy{right:78px;top:210px;font-size:12.5px;color:var(--blue)}
</style>
</head>
<body>
<div class="page">

  <!-- header -->
  <div class="abs brand"><div class="brand-dot"></div><div class="brand-name">Harborview Smile Glow</div></div>
  <div class="abs phone">
    <svg width="18" height="18" viewBox="0 0 24 24"><path d="M6.6 10.8a15 15 0 0 0 6.6 6.6l2.2-2.2a1 1 0 0 1 1-.3 11 11 0 0 0 3.6.6 1 1 0 0 1 1 1V20a1 1 0 0 1-1 1A17 17 0 0 1 3 4a1 1 0 0 1 1-1h3.5a1 1 0 0 1 1 1 11 11 0 0 0 .6 3.6 1 1 0 0 1-.3 1z" fill="#29a9e6"/></svg>
    555-204-7731
  </div>
  <div class="abs btn-book-top">BOOK APPOINTMENT ONLINE</div>
  <div class="abs special">Special Offer : <div class="btn-special">$99 Teeth Whiting Deal <span>(Reg $378)</span></div></div>

  <nav class="abs nav">
    <a class="active">Home</a><a>Our Process</a><a>Photos</a><a>White Smile Club</a><a>Testimonial</a><a>Appointments</a><a>FAQ</a><a>Contact</a><a>Blog</a><a>Buy Now</a>
  </nav>

  <!-- hero -->
  <div class="abs hero" role="img" aria-label="Banner photo of a smiling customer with a staff member holding a best patient sign, and a smiling woman on the right"></div>
  <div class="abs hero-title">GET THAT WHITE SMILE YOU'VE<br>ALWAYS WANTED</div>
  <ul class="abs hero-list">
    <li><svg width="22" height="22" viewBox="0 0 24 24"><path d="M7 3c-3 0-4 3-3 6l2 10c.4 2 2 2 2.4 0l1.1-5h5l1.1 5c.4 2 2 2 2.4 0l2-10c1-3 0-6-3-6-2 0-3 1-5 1S9 3 7 3z" fill="none" stroke="#555" stroke-width="1.5"/></svg>Amazing Results</li>
    <li><svg width="22" height="22" viewBox="0 0 24 24"><path d="M7 3c-3 0-4 3-3 6l2 10c.4 2 2 2 2.4 0l1.1-5h5l1.1 5c.4 2 2 2 2.4 0l2-10c1-3 0-6-3-6-2 0-3 1-5 1S9 3 7 3z" fill="none" stroke="#555" stroke-width="1.5"/></svg>The most effective System</li>
    <li><svg width="22" height="22" viewBox="0 0 24 24"><path d="M7 3c-3 0-4 3-3 6l2 10c.4 2 2 2 2.4 0l1.1-5h5l1.1 5c.4 2 2 2 2.4 0l2-10c1-3 0-6-3-6-2 0-3 1-5 1S9 3 7 3z" fill="none" stroke="#555" stroke-width="1.5"/></svg>More Affordable than the Dentist</li>
  </ul>

  <!-- intro -->
  <section class="abs intro">
    <h1>Harborview Smile Glow</h1>
    <h2>The best price, service and results.</h2>
    <p>Harborview Smile Glow features state-of-the-art technologies that are safe, industry-unique and very cost-effective. Our teeth whitening system utilizes the latest blue light whitening technology. Our Blue Light Systems are calibrated precisely for optimal activation of our exclusive hydrogen peroxide based whitening solution which is manufactured in a FDA registered facility in the USA.</p>
    <p>Our special lighting systems intensify the release of hydroxyl radicals that accelerate the dissipation of tooth stains. The entire teeth whitening process is accelerated and able to be completed in just 45 minutes with instant results.</p>
  </section>

  <!-- booking card -->
  <div class="abs appt-head"><h3>Make an Appoinment<br>Or</h3><p>Call : <b>555-204-7731</b></p></div>
  <div class="abs appt-body">
    <div class="btn-online">
      <svg width="20" height="20" viewBox="0 0 24 24"><rect x="3" y="5" width="18" height="16" rx="2" fill="none" stroke="#1c8fcc" stroke-width="2"/><path d="M3 10h18M8 3v4M16 3v4" stroke="#1c8fcc" stroke-width="2"/></svg>
      BOOK APPOINTMENT ONLINE
    </div>
    <div class="btn-deal">$99 SPECIAL <span>(Reg $378)</span></div>
  </div>

  <!-- how it works -->
  <div class="abs how"></div>
  <div class="abs how-band"><span>We treat children to seniors.</span></div>
  <div class="abs video">
    <div class="video-img" role="img" aria-label="Video still of a child and a woman brushing teeth"></div>
    <div class="video-bar">
      <svg width="398" height="42" viewBox="0 0 398 42">
        <rect x="14" y="13" width="3" height="14" fill="#fff"/><rect x="20" y="13" width="3" height="14" fill="#fff"/>
        <rect x="34" y="20" width="110" height="3" fill="#e02020"/>
        <circle cx="42" cy="21" r="5" fill="#fff"/>
        <rect x="320" y="13" width="44" height="16" rx="8" fill="#fff"/><circle cx="330" cy="21" r="9" fill="#fff" stroke="#29a9e6" stroke-width="2"/>
      </svg>
    </div>
  </div>
  <svg class="abs" style="left:278px;top:1314px" width="40" height="28" viewBox="0 0 40 28"><rect width="40" height="28" rx="6" fill="#111"/><path d="M16 8l10 6-10 6z" fill="#fff"/></svg>
  <h2 class="abs how-title">How It Works</h2>
  <p class="abs how-text">We have a very effective teeth whitening treatment that is guaranteed to get you quick results in about 1 hour. To start the treatment you'll apply a Hydrogen Peroxide based whitening agent to your teeth. We then place our cold blue light directly in front of your exposed teeth for 15 minutes per treatment.</p>
  <div class="abs btn-more">READ MORE</div>

  <!-- compare -->
  <h2 class="abs compare-title">Compare Us</h2>
  <div class="abs cmp">
    <div class="col"><div class="head">LumaPro</div><div class="speed">1-2 Hours</div><div class="cell">Difficult / Dentist</div><div class="cell">$300 - $600</div><div class="cell">Limited Availability</div><div class="cell">Pain &amp; Sensitivity</div></div>
    <div class="col"><div class="head brand-cell">Harborview<br>Smile Glow</div><div class="speed">45 Mins</div><div class="cell">Very Easy</div><div class="cell">$378</div><div class="cell">Appt Only</div><div class="cell">No Pain</div></div>
    <div class="col feat"><div class="head">Features</div><div class="speed">Speed</div><div class="cell">Ease Of Use</div><div class="cell">Cost</div><div class="cell">Availability</div><div class="cell">Pain</div></div>
    <div class="col"><div class="head">GleamFast</div><div class="speed">7 - 14 Days</div><div class="cell">Difficult</div><div class="cell">$300 - $ 600</div><div class="cell">Limited Availability</div><div class="cell">Sensitivity</div></div>
    <div class="col"><div class="head">Home Kits</div><div class="speed">7-30 Days</div><div class="cell">Difficult</div><div class="cell">$ 50- $ 150</div><div class="cell">Store Purchase</div><div class="cell">Sensitivity</div></div>
  </div>

  <!-- testimonial -->
  <blockquote class="abs quote">“Wow... What a terrific experience! Professional, state-of-the-art equipment and Marisol is wonderful! I will definitely be returning when I'm back in Harborview! I highly recommend this service, exceptional!”</blockquote>
  <svg class="abs quote-tail" width="40" height="24" viewBox="0 0 40 24"><path d="M0 0h40L14 24z" fill="#29a9e6"/></svg>
  <div class="abs people">
    <svg width="464" height="90" style="position:absolute;left:0;top:0"><line x1="32" y1="44" x2="432" y2="44" stroke="#bbb"/></svg>
    <div class="arrow-btn" style="left:0;top:28px">«</div>
    <div class="arrow-btn" style="left:432px;top:28px">»</div>
    <div class="av" role="img" aria-label="Customer photo" style="left:58px;top:29px;width:30px;height:30px;background:#c9b7a6"></div>
    <div class="av" role="img" aria-label="Customer photo" style="left:106px;top:16px;width:56px;height:56px;background:#d4b79c"></div>
    <div class="av" role="img" aria-label="Featured customer photo" style="left:188px;top:0;width:88px;height:88px;background:#b89a84;border-color:#fff;box-shadow:0 0 0 2px #ccc"></div>
    <div class="av" role="img" aria-label="Customer photo" style="left:300px;top:16px;width:56px;height:56px;background:#d9c0a3"></div>
    <div class="av" role="img" aria-label="Customer photo" style="left:374px;top:29px;width:30px;height:30px;background:#c3ad9a"></div>
  </div>

  <!-- why choose us -->
  <div class="abs why" role="img" aria-label="Faint background photo of the clinic treatment room"></div>
  <h2 class="abs why-title">Why Choose Us?</h2>
  <div class="abs why-row">
    <div class="why-card on"><div class="icon-ring"><svg width="30" height="44" viewBox="0 0 30 44"><text x="15" y="38" text-anchor="middle" font-family="Roboto,sans-serif" font-size="42" font-weight="700" fill="#111">$</text></svg></div>Price</div>
    <div class="why-card"><div class="icon-ring"><svg width="36" height="34" viewBox="0 0 36 34"><rect x="2" y="20" width="6" height="14" fill="#fff"/><rect x="11" y="14" width="6" height="20" fill="#fff"/><rect x="20" y="8" width="6" height="26" fill="#fff"/><rect x="29" y="2" width="6" height="32" fill="#fff"/></svg></div>Results</div>
    <div class="why-card"><div class="icon-ring"><svg width="34" height="34" viewBox="0 0 24 24"><path d="M7 3c-3 0-4 3-3 6l2 10c.4 2 2 2 2.4 0l1.1-5h5l1.1 5c.4 2 2 2 2.4 0l2-10c1-3 0-6-3-6-2 0-3 1-5 1S9 3 7 3z" fill="none" stroke="#fff" stroke-width="1.6"/></svg></div>No Pain</div>
    <div class="why-card"><div class="icon-ring"><svg width="32" height="32" viewBox="0 0 32 32"><circle cx="16" cy="12" r="8" fill="none" stroke="#fff" stroke-width="2.5"/><rect x="14" y="19" width="4" height="11" fill="#fff"/></svg></div>Service</div>
    <div class="why-card"><div class="icon-ring"><svg width="32" height="32" viewBox="0 0 24 24"><path d="M2 10h4v12H2zM8 22h10a2 2 0 0 0 2-1.6l1.6-7A2 2 0 0 0 19.6 11H14l1-5a2 2 0 0 0-3.6-1.4L8 10z" fill="#fff"/></svg></div>Convenience</div>
  </div>

  <!-- footer -->
  <footer class="abs footer">
    <div class="f-item" style="left:78px"><div class="f-icon"><svg width="20" height="24" viewBox="0 0 20 24"><path d="M10 1a7 7 0 0 0-7 7c0 5 7 14 7 14s7-9 7-14a7 7 0 0 0-7-7z" fill="none" stroke="#333" stroke-width="1.6"/><circle cx="10" cy="8" r="2.5" fill="#333"/></svg></div><div>1470 Harbor Crest Road<br>Ste 110<br>Bayside, CA 90410</div></div>
    <div class="f-item" style="left:500px"><div class="f-icon"><svg width="22" height="22" viewBox="0 0 24 24"><path d="M6.6 10.8a15 15 0 0 0 6.6 6.6l2.2-2.2a1 1 0 0 1 1-.3 11 11 0 0 0 3.6.6 1 1 0 0 1 1 1V20a1 1 0 0 1-1 1A17 17 0 0 1 3 4a1 1 0 0 1 1-1h3.5a1 1 0 0 1 1 1 11 11 0 0 0 .6 3.6 1 1 0 0 1-.3 1z" fill="#333"/></svg></div><div>555-318-4420,</div></div>
    <div class="f-item" style="left:828px"><div class="f-icon"><svg width="24" height="24" viewBox="0 0 24 24"><circle cx="12" cy="12" r="10" fill="none" stroke="#333" stroke-width="2"/><path d="M12 6v6l4 2" stroke="#333" stroke-width="2" fill="none"/></svg></div><div>Monday to Friday: 9am-5pm<br>Saturday: 10am-2pm</div></div>
    <div class="abs f-rule"></div>
    <div class="abs f-links">Home <span>/</span> Our process <span>/</span> Photos <span>/</span> White Smile Club <span>/</span> Testimonial <span>/</span> Contact Us <span>/</span> After care <span>/</span> Consent form espanol <span>/</span> Cancellation policy <span>/</span> Privacy policy</div>
    <div class="abs social"><div><i></i></div><div><i></i></div><div><i></i></div><div><i></i></div><div><i></i></div><div><i></i></div></div>
    <div class="abs copy">© 2017 Harborview Smile Glow All rights reserved.</div>
  </footer>

</div>
</body>
</html>
```